Accounting Practice Business Card Design

I have a logo I am happy for you to use in the design of the Business Card.
You can edit and change colours as you please, I am not fixated on it.
I am looking for a modern and clean overall feel for the finished design.

The business is a small accounting practice who thrives on word of mouth referrals and this card will be given to all current and prospect clients.

Industry/Entity Type

Accountant

Contact Information for Business Card

Marcus Elwin
Level 5, 8 Corvale Ridge Road
ASHGROVE RISE VIC 3187
Phone: 9481 3057
Email: melwin@mrfaccountants.com.au
Web: www.mrfaccountants.com.au

Font styles to use
Serif
Sans Serif

Colors
0555a3
3277b5
85acd3
0393ce
33a6d7
85cae6
00a990
33b8a4
9bcb3c

Requirements
Must have
• "The end to your tax problems begin with us"
• "A referral from you is our greatest compliment"
Nice to have
• Modern clean professional

```html
<!DOCTYPE html>
<html lang="en">
<head>
<meta charset="utf-8">
<title>MRF Accountants – Business Card</title>
<link href="https://fonts.googleapis.com/css2?family=Lato:wght@300;400;700&display=swap" rel="stylesheet">
<style>
  :root {
    --backdrop: #4d5053;
    --card: #18191b;
    --white: #f4f5f6;
    --muted: #8c9095;
    --blue: #33a6d7;
    --blue-deep: #0393ce;
    --teal: #33b8a4;
    --emboss: #222326;
  }
  * { margin: 0; padding: 0; box-sizing: border-box; }
  html, body {
    width: 1200px; height: 1200px; overflow: hidden;
    background: var(--backdrop);
    font-family: "Lato", Arial, sans-serif;
  }
  .stage { position: relative; width: 1200px; height: 1200px; }
  .card {
    position: absolute; left: 180px; width: 840px; height: 480px;
    background: var(--card); border-radius: 40px;
    box-shadow: 0 18px 40px rgba(0,0,0,.35);
    overflow: hidden;
  }
  .card--back { top: 70px; }
  .card--front { top: 650px; }

  /* back */
  .back-mark {
    position: absolute; left: 0; right: 0; top: 170px; text-align: center;
    font-weight: 700; font-size: 58px; letter-spacing: 4px;
    color: var(--emboss);
  }
  .back-tagline {
    position: absolute; left: 0; right: 0; top: 300px; text-align: center;
    font-size: 22px; color: var(--blue); letter-spacing: .3px;
  }

  /* front */
  .brand {
    position: absolute; left: 70px; top: 200px; width: 400px;
  }
  .brand-name {
    font-weight: 700; font-size: 44px; letter-spacing: 2px; line-height: 1;
    color: var(--blue);
  }
  .brand-tagline {
    margin-top: 22px; font-size: 17px; color: var(--white); letter-spacing: .2px;
  }
  .divider {
    position: absolute; left: 500px; top: 90px; width: 2px; height: 300px;
    background: linear-gradient(to bottom, transparent, var(--blue-deep) 50%, transparent);
  }
  .contact { position: absolute; left: 540px; top: 100px; width: 290px; color: var(--white); }
  .contact-name { font-size: 32px; font-weight: 400; }
  .contact-role { margin-top: 4px; font-size: 20px; font-weight: 300; color: var(--muted); }
  .contact-list { list-style: none; margin-top: 36px; }
  .contact-item {
    display: flex; align-items: flex-start; gap: 12px;
    font-size: 15px; line-height: 1.35; margin-bottom: 14px;
  }
  .contact-item--address { margin-bottom: 26px; }
  .contact-icon { flex: 0 0 18px; width: 18px; height: 18px; margin-top: 1px; fill: none; stroke: var(--blue-deep); stroke-width: 1.6; }
  .contact-icon--solid { fill: var(--blue-deep); stroke: none; }
</style>
</head>
<body>
<main class="stage">
  <section class="card card--back" aria-label="Business card back">
    <div class="back-mark">MRF ACCOUNTANTS</div>
    <p class="back-tagline">A referral from you is our greatest compliment.</p>
  </section>

  <section class="card card--front" aria-label="Business card front">
    <div class="brand">
      <div class="brand-name">MRF ACCOUNTANTS</div>
      <p class="brand-tagline">The end to your tax problems begin with us.</p>
    </div>

    <div class="divider"></div>

    <div class="contact">
      <h1 class="contact-name">Marcus Elwin</h1>
      <p class="contact-role">Accountant</p>
      <ul class="contact-list">
        <li class="contact-item contact-item--address">
          <svg class="contact-icon contact-icon--solid" viewBox="0 0 24 24" aria-hidden="true"><path d="M12 2a7 7 0 0 0-7 7c0 5 7 13 7 13s7-8 7-13a7 7 0 0 0-7-7zm0 9.5A2.5 2.5 0 1 1 12 6.5a2.5 2.5 0 0 1 0 5z"/></svg>
          <span>Level 5, 8 Corvale Ridge Road<br>ASHGROVE RISE VIC 3187</span>
        </li>
        <li class="contact-item">
          <svg class="contact-icon contact-icon--solid" viewBox="0 0 24 24" aria-hidden="true"><path d="M6.6 10.8a15 15 0 0 0 6.6 6.6l2.2-2.2a1 1 0 0 1 1-.25 11.4 11.4 0 0 0 3.6.57 1 1 0 0 1 1 1V20a1 1 0 0 1-1 1A17 17 0 0 1 3 4a1 1 0 0 1 1-1h3.5a1 1 0 0 1 1 1c0 1.25.2 2.45.57 3.6a1 1 0 0 1-.25 1z"/></svg>
          <span>9481 3057</span>
        </li>
        <li class="contact-item">
          <svg class="contact-icon" viewBox="0 0 24 24" aria-hidden="true"><rect x="3" y="5" width="18" height="14" rx="1"/><path d="M3 6l9 7 9-7"/></svg>
          <span>melwin@mrfaccountants.com.au</span>
        </li>
        <li class="contact-item">
          <svg class="contact-icon" viewBox="0 0 24 24" aria-hidden="true"><circle cx="12" cy="12" r="9"/><path d="M3 12h18M12 3c3 3 3 15 0 18M12 3c-3 3-3 15 0 18"/></svg>
          <span>www.mrfaccountants.com.au</span>
        </li>
      </ul>
    </div>
  </section>
</main>
</body>
</html>
```